new letterhead/envelope/business card design for law firm

please see attached pdf of current letterhead, envelope and business card. I am also attaching my new logo that I would like to be used. basically, I am looking to refresh and simplify my letterhead/stationary and business card, keeping the following in mind:

overall, I am going for the following look:

-simple,
-modern,
-classy,
-professional

Target Market(s)

law firm clients

Industry/Entity Type

Law Firm

Contact Information for Business Card

see attachment

Font styles to use
Sans Serif

Requirements
Must have
• overall, I am going for the following look:
• -simple,
• -modern,
• -classy,
• -professional
Nice to have
• same as above
Should not have
• no serif fonts

```html
<!DOCTYPE html>
<html lang="en">
<head>
<meta charset="utf-8">
<title>Halden Law — Business Card</title>
<link href="https://fonts.googleapis.com/css2?family=Mulish:wght@400;600;800&display=swap" rel="stylesheet">
<style>
  :root {
    --navy: #13284f;
    --green: #1f5a34;
    --ink: #2a2a2a;
    --card: #ffffff;
    --stage: #ecebe7;
  }
  * { box-sizing: border-box; margin: 0; padding: 0; }
  html, body { width: 1200px; height: 900px; overflow: hidden; }
  body {
    background: var(--stage);
    font-family: "Mulish", Arial, sans-serif;
    position: relative;
  }
  .card {
    position: absolute;
    width: 560px;
    height: 320px;
    background: var(--card);
    box-shadow: 0 10px 28px rgba(0,0,0,0.16);
  }
  .card--back { left: 90px; top: 90px; display: flex; align-items: center; justify-content: center; }
  .card--front { left: 550px; top: 490px; padding: 34px 40px 30px; }

  .brand { display: flex; align-items: center; gap: 12px; }
  .brand__dot { width: 30px; height: 30px; border-radius: 50%; background: var(--green); flex: none; }
  .brand__name {
    font-weight: 800; color: var(--navy);
    font-size: 30px; letter-spacing: 3px; text-transform: uppercase; line-height: 1;
  }
  .card--front .brand { justify-content: center; }
  .card--front .brand__name { font-size: 32px; }
  .brand-rule { width: 230px; height: 2px; background: var(--green); margin: 10px auto 0; }

  .person {
    text-align: center; margin-top: 26px;
    color: var(--green); font-weight: 800; font-size: 15px; letter-spacing: 0.5px; text-transform: uppercase;
  }
  .contact { margin-top: 22px; color: var(--ink); font-size: 14px; line-height: 1.6; }
  .contact__line { display: flex; align-items: center; gap: 6px; white-space: nowrap; }
  .contact__sep { color: #888; margin: 0 4px; }
  .contact .icon { width: 13px; height: 13px; flex: none; fill: none; stroke: var(--green); stroke-width: 1.6; }
  .contact__web strong { color: var(--navy); font-weight: 800; }
  .contact__address { padding-left: 19px; }
</style>
</head>
<body>
  <section class="card card--back" aria-label="Business card back">
    <div class="brand">
      <span class="brand__dot"></span>
      <span class="brand__name">Halden Law</span>
    </div>
  </section>

  <section class="card card--front" aria-label="Business card front">
    <div class="brand">
      <span class="brand__dot"></span>
      <span class="brand__name">Halden Law</span>
    </div>
    <div class="brand-rule"></div>
    <p class="person">Daniel R. Halden, Esq.</p>
    <div class="contact">
      <p class="contact__address">2840 Willow Bend Road, Suite 210, Cary, NC 27513</p>
      <p class="contact__line">
        <svg class="icon" viewBox="0 0 16 16"><path d="M3 2l3 1 1 3-2 1a8 8 0 0 0 4 4l1-2 3 1 1 3-2 1C7 14 2 9 2 4z"/></svg>
        919.555.0142<span class="contact__sep">|</span>
        <svg class="icon" viewBox="0 0 16 16"><rect x="2" y="6" width="12" height="8" rx="1"/><path d="M5 6V2h6v4M5 9h6M5 11h6"/></svg>
        919.555.0187<span class="contact__sep">|</span>
        <svg class="icon" viewBox="0 0 16 16"><rect x="4.5" y="1.5" width="7" height="13" rx="1.5"/><path d="M7 12.5h2"/></svg>
        919.555.0163
      </p>
      <p class="contact__line">
        <svg class="icon" viewBox="0 0 16 16"><rect x="1.5" y="3.5" width="13" height="9" rx="1"/><path d="M1.5 4l6.5 5 6.5-5"/></svg>
        dan@haldenlawpa.com<span class="contact__sep">|</span>
        <svg class="icon" viewBox="0 0 16 16"><circle cx="8" cy="8" r="6.5"/><path d="M1.5 8h13M8 1.5c-3 3.5-3 9.5 0 13M8 1.5c3 3.5 3 9.5 0 13"/></svg>
        <span class="contact__web">www.<strong>haldenlawpa</strong>.com</span>
      </p>
    </div>
  </section>
</body>
</html>
```